Brochure for use by dealers selling gas stoves to residents of small towns and villages

BrightNor company is selling renewable energy solutions and heating for individual customers: photovoltaic panels, heat pumps, ecological gas stoves.

We have prepared a project of the brochure which includes the content we want to pass on. To better understand what we write in it, we suggest you use Lingvaro.example. The brochure will help traders in talks with individual customers: very often simple people, inhabitants of Polish small towns and villages.

We focused on the text and the content we want to convey. Now we need a graphic designer who will improve our message by giving it a graphic form and a more plastic look. The selected texts may change slightly over time and we want to do this ourselves: the final files must therefore be editable. You can change the colors used in our design to your liking.

Our requirements:
1. The booklet must consist of two A4-size sheets (4 pages);
2. CMYK color code;
3. The layout of the brochure (order of information on the pages) must follow the uploaded file;
4. All texts that are in our prototype must also be in the brochure;
5. The brochure has to correspond to the style and aesthetics of Eastern-Central Europe, this concerns possible photos of people (Slavic features), possible photos of surroundings (nature, buildings like in Eastern-Central Europe);
6. The brochure is addressed to the rural population;
7. The texts in the brochure may change slightly over time, and we want to do this ourselves: the final files must therefore be editable.

Current project prototype in figma (with all text):
https://www.designboard.example/file/kQ7mrT2vXp9LwZ4nHbY3sA/BrightNor-Brochure?node-id=0%3A1

Target Market(s)

Polish small towns and villages

Industry/Entity Type

home energy industry

Font styles to use
Sans Serif

Requirements
Must have
• 1. The booklet must consist of two A4-size sheets (4 pages); 2. CMYK color code; 3. The layout of the brochure (order of information on the pages) must follow the uploaded file; 4. All texts that are in our prototype must also be in the brochure; 5. The brochure has to correspond to the style and aesthetics of Eastern-Central Europe, this concerns possible photos of people (Slavic features), possible photos of surroundings (nature, buildings like in Eastern-Central Europe); 6. The brochure is addressed to the rural population; 7. The texts in the brochure may change slightly over time, and we want to do this ourselves: the final files must therefore be editable.

```html
<!DOCTYPE html>
<html lang="pl">
<head>
<meta charset="utf-8">
<title>BrightNor – broszura dotacje</title>
<link rel="stylesheet" href="https://fonts.googleapis.com/css2?family=Roboto:ital,wght@0,400;0,500;0,700;1,400&family=Montserrat:wght@400;700;800&family=Lato:wght@400;700&display=swap">
<style>
  :root {
    --stage: #ececec;
    --navy: #2c3394;
    --panel: #5157a9;
    --orange: #f7952f;
    --orange-text: #f59a3a;
    --white: #ffffff;
    --ink-dark: #2c3394;
  }
  * { box-sizing: border-box; margin: 0; padding: 0; }
  html, body { width: 1200px; height: 642px; overflow: hidden; background: var(--stage); }
  .spread {
    position: absolute; left: 176px; top: 21px;
    width: 849px; height: 600px;
    background: var(--navy);
    font-family: "Roboto", Arial, sans-serif;
    color: var(--white);
    overflow: hidden;
  }
  .abs { position: absolute; }

  /* Left page */
  .calc-title { left: 39px; top: 26px; font-size: 25px; font-weight: 500; color: var(--orange-text); }
  .sub-title { top: 60px; font-size: 19px; font-weight: 500; color: var(--orange-text); }
  .benefits-title { left: 39px; }
  .invest-title { left: 248px; }
  .body-note { top: 91px; font-size: 9.6px; line-height: 12px; }
  .benefits-note { left: 45px; width: 175px; }
  .invest-note { left: 254px; }

  .bar-head {
    left: 35px; top: 136px; width: 354px; height: 23px;
    background: var(--panel); border-radius: 3px;
    font-size: 11px; font-weight: 500; text-align: center; line-height: 23px;
  }
  .grant-table {
    left: 35px; top: 164px; width: 354px; height: 72px;
    background: var(--panel); border-radius: 3px;
  }
  .grant-table .col-head { top: 6px; font-size: 7.5px; font-weight: 500; line-height: 8px; }
  .grant-table .col-head small { font-size: 5.8px; font-weight: 400; display: block; }
  .grant-table .col-basic { left: 162px; }
  .grant-table .col-high { left: 257px; }
  .grant-table .row-label { left: 13px; font-size: 7.5px; font-weight: 500; }
  .grant-table .amount { font-size: 9px; font-weight: 500; }
  .blank-box {
    left: 35px; top: 240px; width: 354px; height: 33px;
    background: var(--panel); border-radius: 3px;
  }
  .blank-box::before { content: ""; position: absolute; left: 6px; top: 4px; width: 1.5px; height: 22px; background: var(--navy); }
  .costs-title { left: 39px; top: 287px; font-size: 19px; font-weight: 500; color: var(--orange-text); }
  .cost-list { left: 35px; top: 317px; width: 354px; list-style: none; }
  .cost-row {
    height: 24px; margin-bottom: 3.7px; background: var(--panel); border-radius: 3px;
    display: flex; justify-content: space-between; align-items: center;
    padding: 0 14px 0 10px; font-size: 11.5px;
  }
  .cost-row.total { font-family: "Montserrat", Arial, sans-serif; font-weight: 700; font-size: 11px; }
  .tech-card {
    left: 35px; top: 520px; width: 159px; height: 60px;
    background: var(--orange); border-radius: 2px; color: var(--ink-dark);
    padding: 8px 11px; font-size: 7px; line-height: 15px;
  }
  .tech-card strong { font-size: 9.5px; display: block; line-height: 14px; }

  /* Right page */
  .cover { left: 424px; top: 0; width: 425px; height: 600px; }
  .cover-photo {
    position: absolute; left: 0; top: 0; width: 425px; height: 360px;
    background:
      radial-gradient(ellipse 55% 30% at 58% 42%, rgba(247,149,47,.75), rgba(44,51,148,0) 70%),
      radial-gradient(ellipse 30% 14% at 58% 30%, rgba(44,51,148,.9), rgba(44,51,148,0) 80%),
      linear-gradient(180deg, #6a5a8f 0%, #43408f 55%, var(--navy) 100%);
  }
  .brand { left: 23px; top: 28px; font-family: "Lato", Arial, sans-serif; font-size: 25px; font-weight: 700; letter-spacing: .5px; }
  .headline { left: 44px; top: 194px; font-size: 32px; line-height: 28px; font-weight: 700; color: var(--orange-text); }
  .headline .small { font-size: 19px; font-weight: 500; }
  .headline .light { font-weight: 500; }
  .tagline { left: 44px; top: 290px; font-size: 14.5px; font-style: italic; color: var(--orange-text); }
  .notice { top: 326px; width: 170px; font-family: "Montserrat", Arial, sans-serif; font-size: 10.8px; line-height: 15.2px; color: var(--orange-text); }
  .notice b { font-weight: 700; }
  .notice-law { left: 44px; }
  .notice-fine { left: 222px; }
  .badges { left: 58px; top: 423px; display: flex; gap: 6px; }
  .badge { height: 31px; background: var(--white); border-radius: 3px; }
  .badge.sq { width: 31px; }
  .badge.wide { width: 69px; }
  .duty { left: 44px; top: 476px; font-family: "Montserrat", Arial, sans-serif; font-size: 12px; font-weight: 800; color: var(--orange-text); }
  .promise { left: 44px; top: 489px; font-family: "Montserrat", Arial, sans-serif; font-size: 25px; font-weight: 800; color: var(--orange-text); white-space: nowrap; }

  /* Bar across the fold */
  .plan-bar {
    left: 261px; top: 536px; width: 386px; height: 37px;
    background: var(--orange); border-radius: 4px; color: var(--ink-dark);
    display: flex; justify-content: space-between; align-items: center; padding: 0 20px 0 31px;
  }
  .plan-bar .bar-brand { font-family: "Lato", Arial, sans-serif; font-size: 16px; font-weight: 700; }
  .plan-bar .plan-name { display: flex; align-items: center; gap: 5px; font-family: "Montserrat", Arial, sans-serif; font-size: 14px; font-weight: 400; }
  .plan-name .mark { width: 13px; height: 13px; background: var(--ink-dark); }
</style>
</head>
<body>
<main class="spread">
  <!-- Inner page: calculation -->
  <section class="calc-page">
    <h1 class="abs calc-title">Szczegółowa kalkulacja</h1>
    <h2 class="abs sub-title benefits-title">Korzyści:</h2>
    <h2 class="abs sub-title invest-title">Inwestycja:</h2>
    <p class="abs body-note benefits-note">Wymiana pieca bez wkładu własnego, niższe rachunki, komfort, bezpieczeństwo.</p>
    <p class="abs body-note invest-note">Opis zestawu</p>

    <div class="abs bar-head">MAKSYMALNA KWOTA DOTACJI</div>
    <div class="abs grant-table">
      <div class="abs col-head col-basic">Poziompodstawowy<small>(do 30% / 45%) kosztów</small></div>
      <div class="abs col-head col-high">Poziompodwyższony<small>(do 60% kosztów)</small></div>
      <div class="abs row-label" style="top:33px">Kocioł gazowy kondensacyjny:</div>
      <div class="abs amount" style="left:183px;top:31px">4500 zł</div>
      <div class="abs amount" style="left:279px;top:31px">9000 zł</div>
      <div class="abs row-label" style="top:51px">Instalacja CO i CWU:</div>
      <div class="abs amount" style="left:183px;top:50px">4500 zł</div>
      <div class="abs amount" style="left:279px;top:50px">9000 zł</div>
    </div>
    <div class="abs blank-box"></div>

    <h2 class="abs costs-title">Koszty i finansowanie:</h2>
    <ul class="abs cost-list">
      <li class="cost-row"><span>Wartość instalacji wraz z montażem:</span><span>zł</span></li>
      <li class="cost-row"><span>Abonament bez dotacji</span><span>zł</span></li>
      <li class="cost-row"><span>Dotacja “Jasne Niebo”</span><span>zł</span></li>
      <li class="cost-row"><span>Dotacja “Ulga termomodernizacyjna”</span><span>zł</span></li>
      <li class="cost-row"><span>Pozostałe dotacje:</span><span>zł</span></li>
      <li class="cost-row total"><span>SUMA DOTACJI:</span><span>zł</span></li>
      <li class="cost-row total"><span>ABONAMENT PO DOTACJACH:</span><span>zł</span></li>
    </ul>

    <div class="abs tech-card">
      <strong>Twój technik</strong>
      Imię, Nazwisko:<br>Telefon:
    </div>
  </section>

  <!-- Cover page -->
  <section class="abs cover">
    <div class="cover-photo" role="img" aria-label="Zbliżenie płonącego palnika kuchenki gazowej w tonacji pomarańczowo-granatowej"></div>
    <div class="abs brand">BrightNor</div>
    <h1 class="abs headline">DOTACJE <span class="small">na</span><br><span class="light">nowoczesne<br>piece gazowe</span></h1>
    <p class="abs tagline">bez wkładu własnego</p>
    <p class="abs notice notice-law">Uchwała antysmogowa nakłada na właścicieli <b>obowiązek wymiany pieców</b> węglowych pozaklasowych do 1 stycznia 2023.</p>
    <p class="abs notice notice-fine">Niezastosowanie się do nowych przepisów będzie wiązać się z kontrolami oraz <b>karą grzywny aż do 5000 zł.</b></p>
    <div class="abs badges">
      <span class="badge sq"></span>
      <span class="badge sq"></span>
      <span class="badge wide"></span>
    </div>
    <p class="abs duty">TWÓJ OBOWIĄZEK / NASZA ODPOWIEDŹ</p>
    <p class="abs promise">nie wydasz ani złotówki</p>
  </section>

  <div class="abs plan-bar">
    <span class="bar-brand">BrightNor</span>
    <span class="plan-name"><span class="mark"></span>EKOPLAN</span>
  </div>
</main>
</body>
</html>
```